Louisiana personal injury attorney needs a postcard design

This will be the first of three post cards to go out to previous clients. We do not have intentions of making all three match/work with each other, but if you have an idea for that, please, let us know! This is for an attorney in Lafayette, LA that specializes in Medical Malpractice and Personal Injury. We would like the front of the post card to focus on those two practice areas and really grab someones attention!

the card in general will say: Glad to have served you, come see us for a free T-shirt, have a cup of coffee with us…

Please use a photo of the office for us to use on the back with a map of the office location (will send location when we pick the winner)

Industry/Entity Type

Legal

Font styles to use
Serif
Sans Serif

Requirements
Must have
• map of location of office. Large image or several images on the front. attention grabbing
Nice to have
• colors that match the logo. clean and easy to follow
Should not have
• should not be messy or too much going on.

```html
<!DOCTYPE html>
<html lang="en">
<head>
<meta charset="utf-8">
<title>Marlow Law Firm – Postcard</title>
<link rel="stylesheet" href="https://fonts.googleapis.com/css2?family=Oswald:wght@500;600&family=Montserrat:wght@300;400;500;600;700&display=swap">
<style>
  :root {
    --gold: #c99a2e;
    --gold-deep: #b8872a;
    --ink: #1f2d2b;
    --text: #222222;
    --white: #ffffff;
    --paper: #e8e5e0;
    --stamp: #e2e2e2;
    --rule: #d6d6d6;
  }
  * { box-sizing: border-box; margin: 0; padding: 0; }
  html, body { width: 1200px; height: 1200px; overflow: hidden; }
  body { background: var(--paper); font-family: "Montserrat", sans-serif; position: relative; }

  .postcard {
    position: absolute;
    left: 180px;
    width: 932px;
    height: 612px;
    background: var(--white);
    transform: scale(0.9013);
    transform-origin: top left;
    overflow: hidden;
    box-shadow: 0 4px 14px rgba(0,0,0,0.12);
  }
  .postcard--front { top: 36px; }
  .postcard--back { top: 612px; }
  .shapes { position: absolute; inset: 0; width: 932px; height: 612px; }

  .abs { position: absolute; }

  /* Front */
  .brand { left: 398px; top: 34px; width: 280px; text-align: center; color: var(--gold); font-weight: 600; }
  .brand__name { display: block; font-size: 62px; line-height: 1; letter-spacing: 2px; }
  .brand__sub { display: block; font-size: 21px; letter-spacing: 9px; margin-top: 6px; }

  .headline { left: 27px; top: 96px; color: var(--white); font-family: "Oswald", sans-serif; font-weight: 600; font-size: 35px; line-height: 37px; letter-spacing: 0.4px; text-transform: uppercase; }
  .tagline { left: 27px; top: 212px; color: var(--white); font-weight: 300; font-size: 23.5px; letter-spacing: 0.4px; }

  .specialty-tag { left: 27px; top: 276px; }
  .specialty-tag__label { position: absolute; left: 17px; top: 4px; color: var(--white); font-weight: 600; font-size: 21px; }

  .practice-list { left: 38px; top: 325px; list-style: none; color: var(--white); font-size: 21px; font-weight: 400; }
  .practice-list li { display: flex; align-items: center; gap: 8px; height: 30px; }

  .offer { left: 32px; top: 500px; border-left: 3px solid var(--ink); padding-left: 10px; }
  .offer__lead { display: block; font-weight: 600; font-size: 24px; line-height: 26px; color: var(--ink); }
  .offer__main { display: block; font-weight: 500; font-size: 19px; line-height: 24px; color: var(--gold); }
  .phone-line { left: 38px; top: 562px; display: flex; align-items: center; gap: 5px; font-size: 16.5px; color: var(--text); }

  .web-front { right: 26px; top: 564px; color: var(--white); font-size: 17px; letter-spacing: 0.3px; }

  /* Back */
  .cta-box { left: 44px; top: 303px; width: 399px; height: 37px; background: var(--ink); border-radius: 6px; color: var(--white); font-family: "Oswald", sans-serif; font-weight: 500; font-size: 24px; line-height: 37px; text-align: center; text-transform: uppercase; }
  .cta-phones { left: 0; width: 493px; top: 342px; display: flex; justify-content: center; align-items: center; gap: 8px; color: var(--white); font-family: "Oswald", sans-serif; font-weight: 500; font-size: 23px; letter-spacing: 0.8px; }
  .office-name { left: 0; width: 493px; top: 397px; text-align: center; color: var(--white); font-weight: 600; font-size: 14px; }
  .office-address { left: 0; width: 493px; top: 415px; text-align: center; color: var(--white); font-weight: 400; font-size: 14.5px; }
  .web-back { left: 0; width: 493px; top: 579px; text-align: center; color: var(--white); font-size: 15px; letter-spacing: 0.3px; }

  .brand--small { left: 540px; top: 56px; width: 140px; }
  .brand--small .brand__name { font-size: 32px; letter-spacing: 1px; }
  .brand--small .brand__sub { font-size: 11px; letter-spacing: 5px; margin-top: 2px; }
  .stamp-box { left: 792px; top: 51px; width: 87px; height: 105px; background: var(--stamp); }
  .address-line { left: 540px; width: 338px; height: 1px; background: var(--rule); }
</style>
</head>
<body>

<section class="postcard postcard--front" aria-label="Postcard front">
  <svg class="shapes" viewBox="0 0 932 612" preserveAspectRatio="none">
    <defs>
      <linearGradient id="meeting-photo" x1="0" y1="0" x2="1" y2="0.6">
        <stop offset="0" stop-color="#e6e9ec"/>
        <stop offset="0.35" stop-color="#9fb6d2"/>
        <stop offset="0.65" stop-color="#d9c7b4"/>
        <stop offset="1" stop-color="#b8b4ad"/>
      </linearGradient>
      <linearGradient id="gavel-photo" x1="0" y1="0" x2="1" y2="1">
        <stop offset="0" stop-color="#7a5a3a"/>
        <stop offset="0.45" stop-color="#2a1c16"/>
        <stop offset="0.75" stop-color="#b08a3e"/>
        <stop offset="1" stop-color="#3d2b22"/>
      </linearGradient>
    </defs>
    <polygon points="0,0 140,0 548,221 147,436 0,500" fill="var(--gold)"/>
    <polygon points="147,436 554,221 932,431 640,612 482,612" fill="url(#meeting-photo)" role="img" aria-label="Photo of an attorney meeting an injured client wearing a neck brace"/>
    <polygon points="560,220 932,73 932,425" fill="url(#gavel-photo)" role="img" aria-label="Photo of a judge's gavel beside a stethoscope"/>
    <polygon points="640,612 932,431 932,612" fill="var(--ink)"/>
    <polyline points="147,436 554,221 932,431" fill="none" stroke="var(--white)" stroke-width="6"/>
    <line x1="554" y1="221" x2="932" y2="70" stroke="var(--white)" stroke-width="6"/>
    <line x1="482" y1="612" x2="147" y2="436" stroke="var(--white)" stroke-width="6"/>
    <line x1="640" y1="612" x2="932" y2="431" stroke="var(--white)" stroke-width="6"/>
  </svg>

  <div class="abs brand"><span class="brand__name">MARLOW</span><span class="brand__sub">LAW FIRM</span></div>

  <h1 class="abs headline">Glad to have<br>served you, come see<br>us for a free T-shirt,</h1>
  <p class="abs tagline">have a cup of coffee with us…</p>

  <div class="abs specialty-tag">
    <svg width="216" height="36" viewBox="0 0 216 36">
      <polygon points="0,0 186,0 200,36 0,36" fill="var(--ink)"/>
      <polygon points="190,0 198,0 214,36 206,36" fill="var(--ink)"/>
    </svg>
    <span class="specialty-tag__label">we specializes</span>
  </div>

  <ul class="abs practice-list">
    <li><svg width="16" height="16" viewBox="0 0 16 16"><circle cx="8" cy="8" r="8" fill="var(--white)"/><path d="M4.5 8.3l2.3 2.2 4.6-4.8" fill="none" stroke="var(--gold)" stroke-width="2"/></svg>Medical Malpractice</li>
    <li><svg width="16" height="16" viewBox="0 0 16 16"><circle cx="8" cy="8" r="8" fill="var(--white)"/><path d="M4.5 8.3l2.3 2.2 4.6-4.8" fill="none" stroke="var(--gold)" stroke-width="2"/></svg>Personal Injury</li>
  </ul>

  <div class="abs offer">
    <span class="offer__lead">GET A FREE</span>
    <span class="offer__main">INITIAL CONSULTATION</span>
  </div>
  <p class="abs phone-line">
    <svg width="12" height="22" viewBox="0 0 12 22"><path d="M7 1.5c-3 0-5.5 4-5.5 9.5S4 20.5 7 20.5l2-.6-1-5-2 .4c-.8-2-.8-6.6 0-8.6l2 .4 1-5z" fill="var(--text)"/></svg>
    800-555-0142 / 337-555-0178
  </p>

  <p class="abs web-front">www.marlowlaw.com</p>
</section>

<section class="postcard postcard--back" aria-label="Postcard back">
  <svg class="shapes" viewBox="0 0 932 612" preserveAspectRatio="none">
    <defs>
      <linearGradient id="office-photo" x1="0" y1="0" x2="0" y2="1">
        <stop offset="0" stop-color="#b9c9da"/>
        <stop offset="0.3" stop-color="#8e99a6"/>
        <stop offset="0.55" stop-color="#3a3d44"/>
        <stop offset="0.85" stop-color="#2f3136"/>
        <stop offset="1" stop-color="#5b7a3e"/>
      </linearGradient>
      <linearGradient id="map-area" x1="0" y1="0" x2="1" y2="1">
        <stop offset="0" stop-color="#f4f4f2"/>
        <stop offset="1" stop-color="#e3e7e3"/>
      </linearGradient>
    </defs>
    <rect x="0" y="0" width="493" height="612" fill="var(--gold)"/>
    <polygon points="0,0 493,0 493,218 246,290 0,218" fill="url(#office-photo)" role="img" aria-label="Photo of the firm's modern dark brick office building under a cloudy sky"/>
    <polyline points="0,218 246,290 493,218" fill="none" stroke="var(--white)" stroke-width="5"/>
    <rect x="0" y="390" width="493" height="100" fill="var(--ink)"/>
    <rect x="43" y="442" width="408" height="132" fill="url(#map-area)" role="img" aria-label="Street map showing the office location"/>
  </svg>

  <div class="abs cta-box">Get a free initial consultation</div>
  <p class="abs cta-phones">
    <svg width="12" height="22" viewBox="0 0 12 22"><path d="M7 1.5c-3 0-5.5 4-5.5 9.5S4 20.5 7 20.5l2-.6-1-5-2 .4c-.8-2-.8-6.6 0-8.6l2 .4 1-5z" fill="var(--white)"/></svg>
    800-555-0142 / 337-555-0178
  </p>
  <p class="abs office-name">MARLOW LAW FIRM</p>
  <p class="abs office-address">220 Bayou Crest Drive Lafayette, LA 70508</p>
  <p class="abs web-back">www.marlowlaw.com</p>

  <div class="abs brand brand--small"><span class="brand__name">MARLOW</span><span class="brand__sub">LAW FIRM</span></div>
  <div class="abs stamp-box"></div>
  <div class="abs address-line" style="top:240px"></div>
  <div class="abs address-line" style="top:323px"></div>
  <div class="abs address-line" style="top:407px"></div>
  <div class="abs address-line" style="top:491px"></div>
</section>

</body>
</html>
```